Mini Leporello with Tartar Recipe from Christmas Apéro

As present from our christmas apero we would like to give our visitors a little booklet of the tartar recipes they enjoyed with us. For this we need a little pocket recipe booklet. ISt should be a Mini-Leparello. You can find the content attached.

Target Market(s)

customers christmas apero

Font styles to use
Other font styles liked:
• FS albert

Requirements
Must have
• each recipe comes from Kalmor or Markus Brenwil - it should show the author
• the format should be 85 x 85 mm and I need a printable file

```html
<!DOCTYPE html>
<html lang="de">
<head>
<meta charset="utf-8">
<title>Tartar-Rezepte – Mini-Leporello 85 × 85 mm</title>
<link href="https://fonts.googleapis.com/css2?family=Lato:wght@400;700&display=swap" rel="stylesheet">
<style>
  :root {
    --bg: #e6e6e6;
    --ice-light: #eef4fa;
    --ice: #dbe7f2;
    --ice-deep: #c6d8ea;
    --navy: #1f4e85;
    --ink: #1e2126;
    --paper: #ffffff;
    --fold: rgba(31,78,133,0.14);
    --panel: 320px;
  }
  * { box-sizing: border-box; margin: 0; padding: 0; }
  html, body { width: 1000px; height: 1200px; overflow: hidden; }
  body {
    background: var(--bg);
    font-family: "Lato", Arial, sans-serif;
    color: var(--ink);
    position: relative;
  }
  .leporello {
    position: absolute;
    left: 20px;
    width: calc(var(--panel) * 3);
    height: var(--panel);
    display: flex;
    box-shadow: 0 8px 24px rgba(0,0,0,0.18);
  }
  .leporello--inside { top: 180px; }
  .leporello--outside { top: 640px; }
  .panel {
    width: var(--panel);
    height: var(--panel);
    flex: 0 0 var(--panel);
    position: relative;
    overflow: hidden;
    background: linear-gradient(180deg, var(--ice-light) 0%, var(--ice) 60%, var(--ice-deep) 100%);
    border-right: 1px solid var(--fold);
    padding: 12px 16px;
  }
  .panel:last-child { border-right: none; }
  .panel--white { background: var(--paper); }
  .panel--flush { padding: 0; }
  .recipe { margin-bottom: 4px; }
  .recipe-title {
    color: var(--navy);
    font-weight: 700;
    font-size: 14px;
    line-height: 1.2;
    letter-spacing: 0.2px;
    margin-bottom: 2px;
  }
  .recipe-text { font-size: 10px; line-height: 1.22; letter-spacing: 0.2px; margin-bottom: 2px; }
  .ingredients { list-style: none; font-size: 10px; line-height: 1.22; letter-spacing: 0.2px; }
  .ingredients li::before { content: "• "; }
  .ingredients--cols { display: grid; grid-template-columns: 1fr 1fr; column-gap: 8px; }
  .ingredients--three { display: grid; grid-template-columns: 1fr 1fr 1fr; column-gap: 8px; }
  .recipe-author {
    font-size: 9px;
    line-height: 1.3;
    color: var(--navy);
    font-weight: 700;
    letter-spacing: 0.3px;
    margin-top: 2px;
  }
  .photo { display: block; }
  .photo--bleed { margin: 4px -16px 5px; width: var(--panel); }
  .intro {
    text-align: center;
    font-size: 9.5px;
    line-height: 1.3;
    letter-spacing: 0.2px;
    margin: 4px 0 6px;
  }
  .contact { display: flex; flex-direction: column; align-items: center; text-align: center; }
  .contact-icon { width: 26px; height: 26px; margin: 6px 0 3px; }
  .contact-line { font-size: 10px; line-height: 1.3; letter-spacing: 0.2px; }
  .contact-line--phone { font-size: 12.5px; }
  .cover-title {
    position: absolute;
    top: 16px; left: 26px; right: 16px;
    color: var(--navy);
    font-weight: 400;
    font-size: 17px;
    line-height: 1.1;
    letter-spacing: 0.8px;
  }
  .cover-year { display: block; font-size: 44px; font-weight: 700; letter-spacing: 2px; margin-top: 2px; }
  .cover-art { position: absolute; left: 0; bottom: 0; width: var(--panel); height: 170px; }
  .tomato-top { width: 100%; height: 28px; }
  .tomato-bottom { position: absolute; left: 0; bottom: 0; width: var(--panel); height: 42px; }
  .thuna-photo { position: absolute; left: 0; bottom: 0; width: var(--panel); height: 118px; }
</style>
</head>
<body>

<section class="leporello leporello--inside">
  <article class="panel">
    <div class="recipe">
      <h2 class="recipe-title">Lachstartar</h2>
      <p class="recipe-text">Geräuchter Lachs fein hacken und mit allen Zutaten mischen.</p>
      <ul class="ingredients ingredients--three">
        <li>Geräuchter Lachs</li><li>Sauerrahm</li><li>Dill</li>
      </ul>
      <p class="recipe-author">Rezept: Kalmor</p>
    </div>
    <svg class="photo photo--bleed" height="46" role="img" aria-label="Foto: Einmachglas mit Gemüsewürfeln, Peperoni und Kartoffeln auf blauem Tisch">
      <defs><linearGradient id="g1" x1="0" x2="1"><stop offset="0" stop-color="#1c4a66"/><stop offset="0.7" stop-color="#256285"/><stop offset="1" stop-color="#8a4a2c"/></linearGradient></defs>
      <rect width="320" height="46" fill="url(#g1)"/>
    </svg>
    <div class="recipe">
      <h2 class="recipe-title">Käsetartar</h2>
      <p class="recipe-text">Den Käse entrinden und in kleine Würfelchen schneiden, Lauch blanchieren, kalt abschrecken. Petersilie und Radieschen hacken danach alle Zutaten mischen und anrichten.</p>
      <ul class="ingredients ingredients--cols">
        <li>Halbhartkäse</li><li>Radieschen</li><li>Petersilie Glattblätterig</li><li>Lauch</li><li>Weinessig</li><li>Senf</li><li>Schwarzer Pfeffer</li><li>Rapsöl</li><li>Rahm</li>
      </ul>
      <p class="recipe-author">Rezept: Markus Brenwil</p>
    </div>
  </article>

  <article class="panel">
    <p class="intro">Unser traditioneller Halden Weihnachtsapéro findet am Donnerstag, dem 15.12.2016, zwischen 17.00 und 20.00 Uhr in unserer Skylounge an der Halden IT Solutions AG statt. In einem aussergewöhnlichen Ambiente können Sie und Ihre Begleitung köstliche Speisen und Getränke beim Apéro Riche geniessen.</p>
    <div class="contact">
      <svg class="contact-icon" viewBox="0 0 40 40"><circle cx="20" cy="20" r="18" fill="none" stroke="var(--navy)" stroke-width="2"/><path d="M20 10a6 6 0 0 1 6 6c0 5-6 11-6 11s-6-6-6-11a6 6 0 0 1 6-6z" fill="none" stroke="var(--navy)" stroke-width="2"/><circle cx="20" cy="16" r="2" fill="var(--navy)"/><path d="M12 29h16" stroke="var(--navy)" stroke-width="2"/></svg>
      <p class="contact-line">Halden IT Solutions AG<br>Birkenweg 12<br>6004 Luzern</p>
      <svg class="contact-icon" viewBox="0 0 40 40"><circle cx="20" cy="20" r="18" fill="none" stroke="var(--navy)" stroke-width="2"/><rect x="14" y="10" width="12" height="20" rx="2" fill="none" stroke="var(--navy)" stroke-width="2"/><circle cx="20" cy="26.5" r="1.2" fill="var(--navy)"/></svg>
      <p class="contact-line contact-line--phone">+41 41 555 01 23</p>
      <svg class="contact-icon" viewBox="0 0 40 40"><circle cx="20" cy="20" r="18" fill="none" stroke="var(--navy)" stroke-width="2"/><rect x="11" y="14" width="18" height="12" fill="var(--navy)"/><path d="M11 14l9 7 9-7" fill="none" stroke="#fff" stroke-width="1.5"/></svg>
      <p class="contact-line">kontakt@haldenag.ch</p>
    </div>
  </article>

  <article class="panel panel--flush">
    <h1 class="cover-title">Tartar-Rezepte<br>vom Halden<br>Weihnachtsapéro<span class="cover-year">2016</span></h1>
    <svg class="cover-art" role="img" aria-label="Foto: verschneiter, bereifter Tannenzweig">
      <defs><linearGradient id="g2" x1="0" y1="0" x2="1" y2="1"><stop offset="0" stop-color="#dfe9f3"/><stop offset="0.5" stop-color="#7d9dc0"/><stop offset="1" stop-color="#2d5784"/></linearGradient></defs>
      <rect width="320" height="170" fill="url(#g2)"/>
    </svg>
  </article>
</section>

<section class="leporello leporello--outside">
  <article class="panel">
    <div class="recipe">
      <h2 class="recipe-title">Rindertartar</h2>
      <p class="recipe-text">Alle Zutaten fein hacken und mischen:</p>
      <ul class="ingredients ingredients--cols">
        <li>Rindsfilet</li><li>Zwiebel</li><li>Essiggurken</li><li>Essig</li><li>Oliven</li><li>Senf</li><li>Peperoni</li><li>Pfeffer</li><li>Kapern</li><li>Salz</li>
      </ul>
      <p class="recipe-author">Rezept: Kalmor</p>
    </div>
    <svg class="photo photo--bleed" height="54" role="img" aria-label="Foto: Holzlöffel mit Gewürzen auf Bambusmatte">
      <defs><linearGradient id="g3" x1="0" y1="0" x2="0" y2="1"><stop offset="0" stop-color="#5e7a5a"/><stop offset="0.6" stop-color="#b89a70"/><stop offset="1" stop-color="#7a5a44"/></linearGradient></defs>
      <rect width="320" height="54" fill="url(#g3)"/>
    </svg>
    <div class="recipe">
      <h2 class="recipe-title">Ligurisches Kalbstartar</h2>
      <p class="recipe-text">Alle Zutaten fein hacken und mischen:</p>
      <ul class="ingredients ingredients--cols">
        <li>Kalbfleisch</li><li>Zitronen</li><li>Olivenoel</li><li>Knoblauch</li><li>Pfeffer</li><li>Salz</li><li>Grosszügig Parmesansplitter</li>
      </ul>
      <p class="recipe-author">Rezept: Markus Brenwil</p>
    </div>
  </article>

  <article class="panel panel--white">
    <svg class="photo tomato-top" role="img" aria-label="Foto: rote Cherrytomaten">
      <ellipse cx="144" cy="14" rx="52" ry="11" fill="#d7342a"/>
    </svg>
    <div class="recipe">
      <h2 class="recipe-title">Tomatentartar</h2>
      <p class="recipe-text">Im Prinzip ist das Tomatentartar ein klassisches Rindstartar, anstelle des Fleisches nimmt man einfach getrocknete / in Oel eingelegte Tomaten. Giessen Sie den Grossteils des Oels ab, aber tupfen Sie die Tomaten nicht trocken. Zerkleinern Sie die Tomaten dann mit dem Pürierstab (nicht zu fein) und geben folgende Zutaten hinzu:</p>
      <ul class="ingredients ingredients--three">
        <li>Eigelb</li><li>Kapern</li><li>Basilikum</li><li>Cognac</li><li>Pfeffer</li><li>Salz</li>
      </ul>
      <ul class="ingredients">
        <li>Weitere Gewürze nach Abschmecken, bzw. je nach Würzigkeit der im Oel eingelegten Tomaten</li>
      </ul>
      <p class="recipe-author">Rezept: Kalmor</p>
    </div>
    <svg class="photo tomato-bottom" role="img" aria-label="Foto: Haufen roter Cherrytomaten">
      <defs><radialGradient id="g4"><stop offset="0" stop-color="#e0473a"/><stop offset="1" stop-color="#a81d17"/></radialGradient></defs>
      <rect width="320" height="42" fill="url(#g4)"/>
    </svg>
  </article>

  <article class="panel">
    <div class="recipe">
      <h2 class="recipe-title">Thunatartar Asiatisch</h2>
      <p class="recipe-text">Dieses Thunatartar bekommt mit folgenden Zutaten eine asiatische Note:</p>
      <ul class="ingredients">
        <li>Zitronengras</li><li>Ingwer</li><li>Basilikum</li><li>Koriander</li><li>Etwas Sojasauce mit Wasabi</li>
      </ul>
      <p class="recipe-text" style="margin-top:4px">Fügen Sie weitere asiatische Saucen gemäss Ihrem Geschmack individuell bei.</p>
      <p class="recipe-author">Rezept: Markus Brenwil</p>
    </div>
    <svg class="photo thuna-photo" role="img" aria-label="Foto: Eigelb in Mehl mit Pasta, Käse und Knoblauch auf dunklem Holz">
      <defs><radialGradient id="g5" cx="0.6" cy="0.4"><stop offset="0" stop-color="#f4f1ea"/><stop offset="0.5" stop-color="#cfc8bb"/><stop offset="1" stop-color="#3a2c24"/></radialGradient></defs>
      <rect width="320" height="118" fill="url(#g5)"/>
    </svg>
  </article>
</section>

</body>
</html>
```